MOLVT Study flyer

I need help designing a flyer for a research study that will include brain imaging in adolescents. The info is in the attached document. The study is called the Marrowby Orchard Lantern Vesper Trail (MOLVT) study. Ideally this would be returned as a document that I can edit in the future as we will have several new recruitment phases (different age groups, etc. I also would love to have a logo designed as part of this project, but I recognize that might be a separate design request.

```html
<!DOCTYPE html>
<html lang="en">
<head>
<meta charset="utf-8">
<title>MOLVT Study – Recruitment Flyer</title>
<link href="https://fonts.googleapis.com/css2?family=Barlow+Semi+Condensed:wght@400;500;600&display=swap" rel="stylesheet">
<style>
  :root {
    --page-bg: #e9e9e9;
    --navy-deep: #0f1628;
    --paper: #ffffff;
    --ink: #111111;
    --orange: #ef5a2a;
    --orange-dark: #e04f22;
    --orange-light: #f4733d;
    --cyan-glow: #4fd8e8;
    --white: #ffffff;
  }
  * { box-sizing: border-box; margin: 0; padding: 0; }
  html, body {
    width: 1200px; height: 1200px; overflow: hidden;
    background: var(--page-bg);
    font-family: "Barlow Semi Condensed", "Arial Narrow", sans-serif;
  }
  .flyer {
    position: absolute; left: 197px; top: 30px;
    width: 806px; height: 1140px; overflow: hidden;
    background: var(--paper);
  }
  .flyer-art, .brain-art { position: absolute; }
  .flyer-art { inset: 0; width: 100%; height: 100%; }
  .brain-art { left: 231px; top: 310px; width: 333px; height: 200px; }
  .headline {
    position: absolute; left: 47px; top: 70px;
    color: var(--white); font-weight: 600; font-size: 37px; line-height: 53px;
  }
  .intro {
    position: absolute; left: 47px; top: 243px; width: 712px;
    color: var(--white); font-size: 17px; line-height: 29px;
  }
  .compensation {
    position: absolute; right: 46px; top: 380px; text-align: right;
    color: var(--white); font-weight: 500;
  }
  .compensation .label { font-size: 28px; line-height: 36px; display: block; }
  .compensation .amount { font-size: 37px; line-height: 44px; display: block; }
  .compensation strong { font-weight: 600; }
  .section-title {
    position: absolute; left: 47px;
    color: var(--ink); font-weight: 600; font-size: 21.5px;
  }
  .section-title.involves { top: 572px; }
  .section-title.eligible { top: 756px; }
  .dash-list {
    position: absolute; left: 47px; width: 705px; list-style: none;
    color: var(--ink); font-size: 17px; line-height: 26.5px;
  }
  .dash-list.involves { top: 626px; }
  .dash-list.eligible { top: 811px; }
  .dash-list li { position: relative; padding-left: 30px; }
  .dash-list li::before { content: "-"; position: absolute; left: 0; }
  .contact {
    position: absolute; left: 0; top: 0; width: 100%; text-align: center; color: var(--white);
  }
  .contact .cta { position: absolute; top: 1017px; width: 100%; font-weight: 600; font-size: 20px; }
  .contact .email { position: absolute; top: 1064px; width: 100%; font-size: 17px; }
</style>
</head>
<body>
<main class="flyer">
  <svg class="flyer-art" viewBox="0 0 806 1140" aria-hidden="true">
    <defs>
      <linearGradient id="sky" x1="0" y1="0" x2="0" y2="1">
        <stop offset="0" stop-color="#0e1427"/>
        <stop offset="0.55" stop-color="#1c2236"/>
        <stop offset="0.8" stop-color="#52566a"/>
        <stop offset="1" stop-color="#ffffff"/>
      </linearGradient>
      <linearGradient id="swoosh" x1="0" y1="0" x2="1" y2="0">
        <stop offset="0" stop-color="#3e4256" stop-opacity="0.8"/>
        <stop offset="0.6" stop-color="#5a5d70" stop-opacity="0.6"/>
        <stop offset="1" stop-color="#8a8c9a" stop-opacity="0"/>
      </linearGradient>
      <linearGradient id="ringFade" gradientUnits="userSpaceOnUse" x1="0" y1="310" x2="0" y2="610">
        <stop offset="0" stop-color="#4fd8e8" stop-opacity="0.45"/>
        <stop offset="0.6" stop-color="#4fd8e8" stop-opacity="0.35"/>
        <stop offset="0.8" stop-color="#4fd8e8" stop-opacity="0"/>
      </linearGradient>
      <radialGradient id="dotGlow">
        <stop offset="0" stop-color="#8eeaf3"/>
        <stop offset="0.55" stop-color="#4fd8e8" stop-opacity="0.85"/>
        <stop offset="1" stop-color="#4fd8e8" stop-opacity="0"/>
      </radialGradient>
      <linearGradient id="orangeBand" x1="0" y1="0" x2="1" y2="0">
        <stop offset="0" stop-color="var(--orange)"/>
        <stop offset="1" stop-color="var(--orange-dark)"/>
      </linearGradient>
    </defs>
    <rect x="0" y="0" width="806" height="680" fill="url(#sky)"/>
    <rect x="0" y="680" width="806" height="460" fill="var(--paper)"/>
    <path class="swoosh" d="M0 440 C 250 455, 550 500, 806 590 L 806 610 C 550 523, 250 477, 0 462 Z" fill="url(#swoosh)"/>
    <circle class="orbit-ring" cx="390" cy="460" r="150" fill="none" stroke="url(#ringFade)" stroke-width="2"/>
    <circle class="orbit-dot" cx="260" cy="535" r="22" fill="url(#dotGlow)"/>
    <path class="orange-wave" d="M0 950 C 330 990, 640 930, 806 770 L 806 1140 L 0 1140 Z" fill="url(#orangeBand)"/>
    <path class="orange-wave-light" d="M420 980 C 600 950, 740 880, 806 800 L 806 830 C 720 910, 600 960, 420 980 Z" fill="var(--orange-light)" fill-opacity="0.5"/>
  </svg>

  <svg class="brain-art" viewBox="0 0 333 200" role="img" aria-label="Glowing line illustration of a human brain with neural network connections">
    <defs>
      <radialGradient id="brainGlow" cx="0.5" cy="0.5" r="0.5">
        <stop offset="0" stop-color="#4fd8e8" stop-opacity="0.3"/>
        <stop offset="1" stop-color="#4fd8e8" stop-opacity="0"/>
      </radialGradient>
    </defs>
    <ellipse cx="166" cy="100" rx="166" ry="100" fill="url(#brainGlow)"/>
  </svg>

  <h1 class="headline">Are you the parent of a child age 10-17?<br>Do they worry or overthink negative emotions?</h1>

  <p class="intro">Harlow Ridge University researchers are seeking girls age 10-17 for a study about brain activity in emotions and decision-making and how they relate to puberty, anxiety and depression</p>

  <p class="compensation">
    <span class="label">Compensation</span>
    <span class="amount">up to <strong>$140</strong></span>
  </p>

  <h2 class="section-title involves">Study participation involves:</h2>
  <ul class="dash-list involves">
    <li>One one-hour interview (online or in-person) where your child will discuss their thoughts</li>
    <li>Online questionnaires (parent and child)</li>
    <li>One two-hour visit where your child will complete an MRI scan, answer questions about their puberty stage, and have a small hair sample taken to study puberty hormones</li>
  </ul>

  <h2 class="section-title eligible">Your child may be eligible if they:</h2>
  <ul class="dash-list eligible">
    <li>Are age 10-17</li>
    <li>Tend to worry or overthink negative thoughts</li>
    <li>have not been diagnosed with psychosis, learning problems, or autism</li>
  </ul>

  <footer class="contact">
    <p class="cta">Interested in participating? Want more information? Please contact us!</p>
    <p class="email">molvtstudy@harlowridge.edu</p>
  </footer>
</main>
</body>
</html>
```